New Zealand Export company needs business cards

We need new business cards to match our new logo for a company based in New Zealand who deal specifically with the Pacific Islands. We source, consolidate and ship products out of New Zealand to the Pacific Islands. Will attach our old ones and also new logo.
Would like the Islands we deal with and the areas of work we have access to, to be included on the business cards.

Contact Information for Business Card

T +64 9 571 3048
F +64 9 571 6285
12-18 Kowhai Lane, Drury, 2113
PO Box 814, Drury, Auckland 2247, New Zealand
www.falconfreight.example.nz
E sales@falconfreight.example.nz

Font styles to use
Sans Serif

Colors
85abd2
33a6d7
ffffff

Requirements
Must have
• A company of PWM

```html
<!DOCTYPE html>
<html lang="en">
<head>
<meta charset="utf-8">
<title>Falcon Freight – Business Cards</title>
<link rel="stylesheet" href="https://fonts.googleapis.com/css2?family=Roboto:wght@400;500;700&display=swap">
<style>
  :root {
    --page: #3a3a3a;
    --card: #2a2a2b;
    --brand-blue: #1b63b5;
    --sky-blue: #33a6d7;
    --white: #ffffff;
    --muted: #e6e6e6;
  }
  * { box-sizing: border-box; margin: 0; padding: 0; }
  html, body {
    width: 1200px; height: 960px; overflow: hidden;
    background: var(--page);
    font-family: "Roboto", Arial, sans-serif;
  }
  .sheet {
    width: 1200px; height: 960px;
    display: flex; flex-direction: column; align-items: center; justify-content: center;
    gap: 60px;
  }
  .card {
    position: relative;
    width: 700px; height: 400px;
    background: var(--card);
    overflow: hidden;
    box-shadow: 0 12px 30px rgba(0,0,0,.45);
  }

  /* Front */
  .card-front .brand {
    position: absolute; top: 140px; left: 0; right: 0;
    display: flex; align-items: center; justify-content: center; gap: 18px;
  }
  .brand-square { width: 46px; height: 46px; background: var(--brand-blue); }
  .brand-name {
    font-size: 50px; font-weight: 700; letter-spacing: 2px;
    color: var(--brand-blue); line-height: 1;
  }
  .card-front .tagline {
    position: absolute; top: 290px; left: 0; right: 0;
    text-align: center; font-size: 22px; font-weight: 500;
    color: var(--sky-blue);
  }

  /* Back */
  .card-back .brand {
    position: absolute; top: 44px; left: 40px;
    display: flex; align-items: center; gap: 10px;
  }
  .card-back .brand-square { width: 24px; height: 24px; }
  .card-back .brand-name { font-size: 26px; letter-spacing: 1px; }

  .person { position: absolute; top: 128px; left: 56px; }
  .person-name {
    font-size: 32px; font-weight: 700; color: var(--sky-blue); letter-spacing: .5px;
  }
  .person-role { font-size: 20px; color: var(--white); margin-top: 4px; padding-left: 14px; }

  .contacts {
    position: absolute; top: 238px; left: 56px;
    list-style: none;
  }
  .contacts li {
    display: flex; align-items: center; gap: 14px;
    font-size: 19px; color: var(--white); height: 28px;
  }
  .contacts svg { width: 18px; height: 18px; flex: none; fill: var(--sky-blue); }
  .contacts .highlight { color: var(--sky-blue); }

  .address {
    position: absolute; top: 190px; right: 40px;
    text-align: right; font-size: 19px; line-height: 1.45; color: var(--muted);
  }

  .band { position: absolute; height: 14px; }
  .band-sky { left: 0; width: 400px; bottom: 0; background: var(--sky-blue); }
  .band-brand { left: 400px; right: 0; bottom: 16px; background: var(--brand-blue); }
</style>
</head>
<body>
<main class="sheet">

  <section class="card card-front">
    <div class="brand">
      <span class="brand-square"></span>
      <span class="brand-name">FALCON FREIGHT</span>
    </div>
    <p class="tagline">A company of PWM</p>
  </section>

  <section class="card card-back">
    <div class="brand">
      <span class="brand-square"></span>
      <span class="brand-name">FALCON FREIGHT</span>
    </div>

    <div class="person">
      <h1 class="person-name">DANIEL HART</h1>
      <p class="person-role">Sales Manager</p>
    </div>

    <ul class="contacts">
      <li>
        <svg viewBox="0 0 24 24" aria-hidden="true"><path d="M6.6 10.8a15.1 15.1 0 0 0 6.6 6.6l2.2-2.2a1 1 0 0 1 1-.25 11.4 11.4 0 0 0 3.6.57 1 1 0 0 1 1 1V20a1 1 0 0 1-1 1A17 17 0 0 1 3 4a1 1 0 0 1 1-1h3.5a1 1 0 0 1 1 1c0 1.25.2 2.45.57 3.57a1 1 0 0 1-.25 1z"/></svg>
        +64 9 571 3048
      </li>
      <li>
        <svg viewBox="0 0 24 24" aria-hidden="true"><path d="M6 2h12v5H6zM4 8h16a2 2 0 0 1 2 2v6h-4v-3H6v3H2v-6a2 2 0 0 1 2-2zm3 7h10v7H7z"/></svg>
        +64 9 571 6285
      </li>
      <li>
        <svg viewBox="0 0 24 24" aria-hidden="true"><path d="M2 5h20v14H2zm2 2v.5l8 5 8-5V7z"/></svg>
        sales@falconfreight.example.nz
      </li>
      <li>
        <svg viewBox="0 0 24 24" aria-hidden="true"><circle cx="12" cy="12" r="10"/></svg>
        <span>www.<span class="highlight">falconfreight</span>.example.nz</span>
      </li>
    </ul>

    <address class="address" style="font-style:normal">
      12-18 Kowhai Lane, Drury, 2113<br>
      PO Box 814, Drury<br>
      Auckland 2247, New Zealand
    </address>

    <span class="band band-brand"></span>
    <span class="band band-sky"></span>
  </section>

</main>
</body>
</html>
```